Local Flower Farm Needs Business Card Design

I need business cards designed for a flower farm based in Eudora, Kansas.
Business Info:
We are a local cut flower farm located in Eudora, Kansas, founded by Darla Hoffstrom. What started as a passion for agriculture and search for more joy in daily life has blossomed into a small business dedicated to providing the community with beautiful, fresh, and sustainable flowers. We specialize in local, seasonal blooms, ensuring that every petal reflects the care and dedication we pour into our craft. Our mission is to deliver the highest quality flowers directly to our customers through local farmers markets and to florists who share our commitment to sustainability. Join us in celebrating the beauty of nature, one bloom at a time!
Contact Details:
Darla Hoffstrom
Owner
Phone 913-555-0147
Facebook: Lorabelle Quinn Blossoms
Instagram: @LorabelleQuinnBlossoms
Website: LorabelleQuinnBlossoms.example
Target Market(s)
Wholesale to Florists and Direct to Consumer via Farmers Market
Industry/Entity Type
Florist, Farm
Contact Information for Business Card
Name, Contact Info, Logo
Look and feel

```html
<!DOCTYPE html>
<html lang="en">
<head>
<meta charset="utf-8">
<title>Lorabelle Quinn Blossoms — Business Card</title>
<link href="https://fonts.googleapis.com/css2?family=Montserrat:wght@400;500;700&display=swap" rel="stylesheet">
<style>
  :root {
    --stage: #1a1a1a;
    --card-dark: #0e2529;
    --card-light: #2f4c52;
    --ink: #ffffff;
    --ink-soft: #e6eeee;
  }
  * { box-sizing: border-box; margin: 0; padding: 0; }
  html, body {
    width: 1200px; height: 900px; overflow: hidden;
    background: var(--stage);
    font-family: "Montserrat", sans-serif;
    color: var(--ink);
  }
  .stage {
    position: relative; width: 1200px; height: 900px;
  }
  .card {
    position: absolute; left: 260px;
    width: 680px; height: 389px;
    background: linear-gradient(135deg, var(--card-dark) 0%, #173539 55%, var(--card-light) 100%);
    box-shadow: 0 14px 30px rgba(0,0,0,.55);
  }
  .card--front { top: 40px; }
  .card--back { top: 470px; }

  .brand-seal {
    position: absolute;
    border: 1.5px solid var(--ink);
    border-radius: 50%;
    display: flex; align-items: center; justify-content: center;
    text-align: center;
  }
  .brand-seal__name {
    font-family: "Montserrat", sans-serif;
    font-weight: 500;
    color: var(--ink);
    letter-spacing: .18em;
    text-transform: uppercase;
    line-height: 1.5;
  }
  .card--front .brand-seal {
    width: 250px; height: 250px; left: 215px; top: 70px;
  }
  .card--front .brand-seal__name { font-size: 17px; }
  .card--back .brand-seal {
    width: 280px; height: 280px; left: 370px; top: 62px;
  }
  .card--back .brand-seal__name { font-size: 19px; }

  .contact {
    position: absolute; left: 44px; top: 38px; width: 330px;
  }
  .contact__name {
    font-weight: 700; font-size: 21px; letter-spacing: .04em;
    text-transform: uppercase;
  }
  .contact__role {
    font-size: 12px; font-weight: 400; letter-spacing: .06em;
    text-transform: uppercase; color: var(--ink-soft); margin-top: 2px;
  }
  .contact__address {
    font-style: normal; font-size: 13.5px; line-height: 1.35;
    margin-top: 24px; color: var(--ink-soft);
  }
  .contact__list { list-style: none; margin-top: 18px; }
  .contact__item {
    display: flex; align-items: center; gap: 9px;
    font-size: 13.5px; line-height: 1.3; margin-bottom: 6px;
    color: var(--ink-soft); white-space: nowrap;
  }
  .contact__icon { width: 13px; height: 13px; flex: none; }
  .contact__rule {
    width: 10px; height: 1.5px; background: var(--ink); margin: 10px 0 12px;
  }
  .social-dot {
    width: 12px; height: 12px; border-radius: 50%;
    border: 1.5px solid var(--ink); flex: none;
  }
</style>
</head>
<body>
<main class="stage">
  <section class="card card--front" aria-label="Card front">
    <div class="brand-seal">
      <span class="brand-seal__name">Lorabelle<br>Quinn<br>Blossoms</span>
    </div>
  </section>

  <section class="card card--back" aria-label="Card back">
    <div class="contact">
      <h1 class="contact__name">Darla Hoffstrom</h1>
      <p class="contact__role">Owner</p>
      <address class="contact__address">
        2140 Meadowlark Ln<br>STE 12<br>Eudora, KS 66000
      </address>
      <ul class="contact__list">
        <li class="contact__item">
          <svg class="contact__icon" viewBox="0 0 16 16" aria-hidden="true"><path fill="#fff" d="M3.6 1.2l2.3 2.6-1.3 1.9c.9 2 2.5 3.6 4.6 4.6l1.9-1.3 2.6 2.3-1.5 2.5C7.4 13.6 2.4 8.6 1.1 2.7z"/></svg>
          913-555-0147
        </li>
        <li class="contact__item">
          <svg class="contact__icon" viewBox="0 0 16 16" aria-hidden="true"><rect x="1" y="3" width="14" height="10" fill="#fff"/><path d="M1 3l7 5.5L15 3" fill="none" stroke="#173539" stroke-width="1.4"/></svg>
          info@LorabelleQuinnBlossoms.example
        </li>
        <li class="contact__item">
          <svg class="contact__icon" viewBox="0 0 16 16" aria-hidden="true"><g fill="none" stroke="#fff" stroke-width="1.3"><circle cx="8" cy="8" r="6.5"/><ellipse cx="8" cy="8" rx="2.8" ry="6.5"/><path d="M1.5 8h13M2.6 4.6h10.8M2.6 11.4h10.8"/></g></svg>
          www.LorabelleQuinnBlossoms.example
        </li>
      </ul>
      <div class="contact__rule"></div>
      <ul class="contact__list">
        <li class="contact__item"><span class="social-dot"></span>Lorabelle Quinn Blossoms</li>
        <li class="contact__item"><span class="social-dot"></span>@LorabelleQuinnBlossoms</li>
      </ul>
    </div>
    <div class="brand-seal">
      <span class="brand-seal__name">Lorabelle<br>Quinn<br>Blossoms</span>
    </div>
  </section>
</main>
</body>
</html>
```